modernized upgrade to existing squarespace site

Hello! I have the following page for my consulting firm: https://hollinbrookcounsel.com/ Would love to upgrade to something more modern/attractive like here: https://www.pemberlowgroup.com/ or https://brightquillstudio.com/ , but I am open to creativity. Would like to retain the logo look and color theme from the logo. The rest can be left to creative discretion.

```html
<!DOCTYPE html>
<html lang="en">
<head>
<meta charset="utf-8">
<title>Hollinbrook Counsel</title>
<link href="https://fonts.googleapis.com/css2?family=Rubik:wght@500;600&family=Outfit:wght@300;400;500;600&display=swap" rel="stylesheet">
<style>
:root{
  --rose:#c48f84;
  --rose-dark:#b57b70;
  --blush:#f5e8e6;
  --ink:#1d1b1c;
  --text:#2b2a2a;
  --muted:#6b6466;
  --white:#ffffff;
  --footer:#262224;
  --line:#cfc8c6;
}
*{margin:0;padding:0;box-sizing:border-box}
html,body{width:1200px;height:4409px;overflow:hidden}
body{position:relative;font-family:'Outfit',sans-serif;color:var(--text);background:var(--white)}
.abs{position:absolute}
h1,h2,h3{font-family:'Rubik',sans-serif;font-weight:500;color:var(--ink)}
.btn{position:absolute;display:flex;align-items:center;justify-content:center;font-size:12px;font-weight:500;background:var(--rose);color:var(--ink)}

/* hero */
.hero{left:0;top:0;width:1200px;height:618px;background:linear-gradient(180deg,#f4f4f4 0%,#b9bcc0 14%,#6d7a80 30%,#3e4a4c 55%,#2b3131 80%,#3a3a36 100%)}
.brand{display:flex;align-items:center;gap:10px}
.brand-mark{width:58px;height:58px;border:2px solid var(--rose)}
.brand-name{font-family:'Outfit',sans-serif;font-weight:500;font-size:30px;line-height:1;letter-spacing:3px;color:var(--ink)}
.brand-name small{display:block;font-size:13px;letter-spacing:2px;margin-top:3px}
.nav{left:560px;top:42px;display:flex;gap:20px;font-size:12px;font-weight:500;color:var(--ink)}
.nav .on{color:var(--rose);text-decoration:underline}
.nav-cta{left:943px;top:30px;width:116px;height:42px}
.hero-title{left:0;top:205px;width:1200px;text-align:center;font-size:38px;line-height:51px;color:var(--white);font-weight:600}
.hero-sub{left:240px;top:320px;width:720px;text-align:center;font-size:13px;line-height:22px;color:var(--white)}
.hero-btn{left:538px;top:385px;width:124px;height:41px;background:var(--white)}
.mouse{left:586px;top:505px}

/* research */
.blush-band{left:0;top:618px;width:1200px;height:755px;background:var(--blush)}
.card-left{left:0;top:664px;width:1125px;height:661px;background:var(--white)}
.photo{border-radius:0}
.ph-research{left:87px;top:741px;width:509px;height:507px;background:linear-gradient(135deg,#9a5a48 0%,#b9bbbe 35%,#d9dfe6 65%,#8e7c6e 100%)}
.sec-title{font-size:31px;line-height:47px}
.sec-text{font-size:14px;line-height:26px;color:var(--ink)}
.side-rail{width:12px}
.dot{width:12px;height:12px;border:1.5px solid var(--rose);border-radius:50%;margin-bottom:10px}
.rail-line{width:2px;margin:6px auto 16px;background:var(--rose)}

/* partners */
.partners-title{left:0;top:1448px;width:1200px;text-align:center;font-size:34px}
.badge{top:1550px;height:105px;background:#d9d6d6}

/* pr */
.rose-band{left:0;top:1751px;width:1200px;height:755px;background:var(--rose)}
.card-right{left:72px;top:1798px;width:1128px;height:662px;background:var(--white)}
.ph-pr{left:601px;top:1876px;width:508px;height:507px;background:linear-gradient(150deg,#d9dde0 0%,#3c4654 35%,#b07c4c 65%,#c99a6a 100%)}

/* services */
.center-title{left:0;width:1200px;text-align:center;font-size:34px}
.svc{top:2671px;width:293px;height:308px;text-align:center;padding-top:48px}
.svc.white{background:var(--white);box-shadow:0 2px 14px rgba(0,0,0,.08)}
.svc.tint{background:var(--blush)}
.svc-icon{width:86px;height:86px;border-radius:50%;background:var(--rose);margin:0 auto;display:flex;align-items:center;justify-content:center}
.svc h3{font-size:17px;margin-top:26px}
.svc p{font-size:12px;line-height:20px;margin:10px auto 0;width:230px;color:var(--ink)}
.svc a{display:inline-block;margin-top:16px;font-size:14px;font-weight:500;color:var(--rose);text-decoration:underline}

/* testimonials */
.quote{top:3159px;width:383px;height:162px;border:2px solid var(--line);padding:20px 24px;font-size:11px;line-height:20px;color:var(--ink)}
.quote-mark{position:absolute;top:-14px;left:26px;width:26px;height:26px;border-radius:50%;background:var(--rose);color:var(--white);font-family:'Rubik',sans-serif;font-size:18px;display:flex;align-items:center;justify-content:center}
.quote-end{position:absolute;right:40px;bottom:-10px;background:var(--white);padding:0 6px;color:#999;font-size:18px;font-family:'Rubik',sans-serif}
.person{top:3341px;display:flex;align-items:center;gap:10px;font-size:13px;color:var(--rose)}
.avatar{width:32px;height:32px;border-radius:50%;background:linear-gradient(135deg,#6e6a64,#3a4d48)}
.arrow{top:3228px;width:22px;height:22px;border-radius:50%;background:#e6d3cf;display:flex;align-items:center;justify-content:center}

/* news */
.news{top:3547px;width:291px;height:336px;border:2px solid var(--line);padding:6px}
.news-img{height:173px}
.news h4{font-size:12px;font-weight:600;line-height:23px;color:var(--ink);margin:16px 6px 0}
.news p{font-size:12px;color:var(--muted);margin:10px 6px 0;letter-spacing:.3px}

/* footer */
.footer{left:0;top:4057px;width:1200px;height:352px;background:var(--footer);color:var(--white)}
.foot-h{font-family:'Outfit',sans-serif;font-weight:500;font-size:18px;letter-spacing:.5px}
.foot-item{display:flex;gap:10px;font-size:12px;line-height:17px;margin-top:20px}
.foot-links li{list-style:none;font-size:12px;margin-top:12px}
.vline{width:1px;background:#4a4446}
.foot-brand .brand-mark{border-color:var(--white)}
.foot-brand .brand-name{color:var(--white)}
.copy{left:0;top:4375px;width:1200px;text-align:center;font-size:12px}
.hr{left:140px;top:4358px;width:920px;height:1px;background:#4a4446}
</style>
</head>
<body>

<!-- hero -->
<section class="abs hero" role="img" aria-label="City skyline with high-rise towers beneath misty mountains"></section>
<div class="abs brand" style="left:140px;top:22px">
  <div class="brand-mark"></div>
  <div class="brand-name">HOLLINBROOK<small>COUNSEL</small></div>
</div>
<nav class="abs nav"><span class="on">Home</span><span>Services</span><span>Research</span><span>The Institute</span><span>In the News</span></nav>
<div class="btn nav-cta">Contact</div>
<h1 class="abs hero-title">Macroeconomic &amp; policy analytics for today’s<br>turbulent environment.</h1>
<p class="abs hero-sub">The Hollinbrook Policy Institute (HPI) is an independent non-profit organization that partners with private think tanks, academic institutions</p>
<div class="btn hero-btn">Get Started</div>
<svg class="abs mouse" width="28" height="56" viewBox="0 0 28 56"><rect x="2" y="2" width="24" height="36" rx="12" fill="none" stroke="#fff" stroke-width="3"/><line x1="14" y1="10" x2="14" y2="20" stroke="#fff" stroke-width="3" stroke-linecap="round"/><path d="M8 44 L14 50 L20 44" fill="none" stroke="#fff" stroke-width="3"/></svg>

<!-- research -->
<div class="abs blush-band"></div>
<div class="abs card-left"></div>
<div class="abs photo ph-research" role="img" aria-label="Two analysts reviewing documents together at a desk"></div>
<h2 class="abs sec-title" style="left:649px;top:810px;width:440px">Sophisticated research<br>&amp; atypical analyses for<br>improved communications.</h2>
<p class="abs sec-text" style="left:650px;top:970px;width:420px">From municipal to federal, our fiscal policy expertise has spanned decades, while our analytical work has covered the hyperlocal considerations of small towns to the macroeconomic effects related to broader national fiscal policy concerns, as well as transnational implications.</p>
<div class="btn" style="left:650px;top:1126px;width:115px;height:42px">Learn More</div>
<div class="abs side-rail" style="left:1150px;top:712px">
  <div class="dot"></div><div class="dot"></div>
  <div class="rail-line" style="height:460px"></div>
  <div class="dot"></div><div class="dot"></div>
</div>

<!-- partners -->
<h2 class="abs partners-title">Our Partners</h2>
<div class="abs badge" style="left:140px;width:155px" aria-hidden="true"></div>
<div class="abs badge" style="left:342px;width:108px"></div>
<div class="abs badge" style="left:534px;width:130px"></div>
<div class="abs badge" style="left:748px;width:78px"></div>
<div class="abs badge" style="left:905px;width:155px"></div>

<!-- pr -->
<div class="abs rose-band"></div>
<div class="abs card-right"></div>
<h2 class="abs sec-title" style="left:140px;top:1945px;width:440px">Proprietary public relations<br>tools that guarantee<br>media visibility.</h2>
<p class="abs sec-text" style="left:140px;top:2104px;width:420px">Our services suite focuses on providing exclusive, custom research and analytics to a select number of clients. We do so by outlining a sophisticated research plan, building teams of industry experts, and providing final analyses catered to your preferred audience.</p>
<div class="btn" style="left:140px;top:2260px;width:116px;height:42px">Learn More</div>
<div class="abs photo ph-pr" role="img" aria-label="Smiling consultant presenting charts at a conference table"></div>
<div class="abs side-rail" style="left:33px;top:1846px">
  <div class="dot"></div><div class="dot"></div>
  <div class="rail-line" style="height:460px;background:var(--ink)"></div>
  <div class="dot"></div><div class="dot"></div>
</div>

<!-- services -->
<h2 class="abs center-title" style="top:2584px">Our Services</h2>
<div class="abs svc white" style="left:140px">
  <div class="svc-icon"><svg width="44" height="44" viewBox="0 0 44 44" fill="none" stroke="#fff" stroke-width="2"><rect x="6" y="10" width="26" height="20" rx="2"/><polyline points="10,26 16,20 20,23 27,15"/><circle cx="30" cy="28" r="6"/><line x1="34" y1="32" x2="39" y2="37"/></svg></div>
  <h3>Analytics &amp; Messaging</h3>
  <p>Our communications team can develop influential messaging,</p>
  <a>Read More</a>
</div>
<div class="abs svc tint" style="left:454px">
  <div class="svc-icon"><svg width="44" height="44" viewBox="0 0 44 44" fill="none" stroke="#fff" stroke-width="2"><circle cx="17" cy="18" r="6"/><path d="M7 38 C8 29 26 29 27 38"/><rect x="24" y="6" width="14" height="10" rx="2"/><line x1="27" y1="10" x2="35" y2="10"/></svg></div>
  <h3>Customized Reports</h3>
  <p>From succinct summations of economic and policy impact to full-length analyses,</p>
  <a>Read More</a>
</div>
<div class="abs svc tint" style="left:765px">
  <div class="svc-icon"><svg width="44" height="44" viewBox="0 0 44 44" fill="none" stroke="#fff" stroke-width="2"><rect x="8" y="8" width="28" height="20" rx="1"/><line x1="22" y1="28" x2="22" y2="36"/><line x1="14" y1="38" x2="30" y2="38"/><line x1="13" y1="14" x2="31" y2="14"/><line x1="13" y1="19" x2="26" y2="19"/><line x1="13" y1="24" x2="22" y2="24"/></svg></div>
  <h3>Proprietary Surveys</h3>
  <p>Exclusive, custom-designed surveys can enrich your databank, while maintaining</p>
  <a>Read More</a>
</div>

<!-- testimonials -->
<h2 class="abs center-title" style="top:3058px">What Our Clients Say</h2>
<div class="abs arrow" style="left:141px"><svg width="8" height="10" viewBox="0 0 8 10"><path d="M6 1 L2 5 L6 9" fill="none" stroke="#b57b70" stroke-width="1.6"/></svg></div>
<div class="abs arrow" style="left:1035px"><svg width="8" height="10" viewBox="0 0 8 10"><path d="M2 1 L6 5 L2 9" fill="none" stroke="#b57b70" stroke-width="1.6"/></svg></div>
<div class="abs quote" style="left:197px"><span class="quote-mark">“</span>“ Lorem ipsum dolor sit amet, consectetur adipiscing elit. Nam fermentum in diam et congue. Morbi aliquet posuere ligula tempus aliquet. Duis rutrum vel tortor at consectetur. Integer interdum ex ac magna facilisis, vel vestibulum lectus luctus. Nunc nibh libero, bibendum tincidunt vulputate sed, pulvinar sit amet leo....(+) ”<span class="quote-end">”</span></div>
<div class="abs quote" style="left:618px"><span class="quote-mark">“</span>“Lorem ipsum dolor sit amet, consectetur adipiscing elit. Nam fermentum in diam et congue. Morbi aliquet posuere ligula tempus aliquet. Duis rutrum vel tortor at consectetur. Integer interdum ex ac magna facilisis, vel vestibulum lectus luctus. Nunc nibh libero, bibendum tincidunt vulputate sed, pulvinar sit amet leo.......(+)”<span class="quote-end">”</span></div>
<div class="abs person" style="left:216px"><div class="avatar" role="img" aria-label="Client portrait"></div>Ravi Menon</div>
<div class="abs person" style="left:644px"><div class="avatar" role="img" aria-label="Client portrait"></div>Dana Pell</div>

<!-- news -->
<h2 class="abs center-title" style="top:3458px">Latest News</h2>
<article class="abs news" style="left:140px">
  <div class="news-img" role="img" aria-label="Hands reviewing printed charts with a pen" style="background:linear-gradient(135deg,#dfe7ee,#9fb2c6 60%,#e8ecef)"></div>
  <h4>commissioned the new economic research report by Hollinbrook Counsel to study the industry’s . . . economic impact on states</h4>
  <p>Device Sourcing Quarterly</p>
</article>
<article class="abs news" style="left:454px">
  <div class="news-img" role="img" aria-label="Lab technician in protective suit working under red light" style="background:linear-gradient(135deg,#2c4f8a,#c23a3a 55%,#e9e3e6)"></div>
  <h4>New Data Finds Medtech Industry Thrives in the Sunshine State.</h4>
  <p>Coastal Health Ledger</p>
</article>
<article class="abs news" style="left:764px">
  <div class="news-img" role="img" aria-label="Researcher examining data on a monitor in a laboratory" style="background:linear-gradient(135deg,#4d6f93,#1f3d63 55%,#9ab4cc)"></div>
  <h4>Medical Technology Industry Continues to Create High-Paying Jobs at Small Businesses Throughout Pandemic.</h4>
  <p>Scan Tech Review</p>
</article>
<div class="btn" style="left:532px;top:3929px;width:136px;height:41px">View All News</div>

<!-- footer -->
<footer class="abs footer">
  <div class="abs" style="left:143px;top:70px;width:240px">
    <div class="foot-h">CONTACT DETAILS</div>
    <div class="foot-item"><svg width="16" height="18" viewBox="0 0 16 18"><path d="M8 1 C4 1 2 4 2 7 C2 11 8 17 8 17 C8 17 14 11 14 7 C14 4 12 1 8 1Z" fill="none" stroke="#fff" stroke-width="1.5"/><circle cx="8" cy="7" r="2" fill="#fff"/></svg><span>48 Alder Row, Suite 210<br>Fairhaven, MA 02719</span></div>
    <div class="foot-item"><svg width="16" height="14" viewBox="0 0 16 14"><rect x="1" y="2" width="14" height="10" fill="none" stroke="#fff" stroke-width="1.5"/><path d="M1 2 L8 8 L15 2" fill="none" stroke="#fff" stroke-width="1.5"/></svg><span>Email<br>info@hollinbrookcounsel.com</span></div>
    <div class="foot-item"><svg width="16" height="16" viewBox="0 0 16 16"><path d="M3 1 L6 1 L7 5 L5 6 C6 8 8 10 10 11 L11 9 L15 10 L15 13 C15 14 14 15 13 15 C6 14 2 10 1 3 C1 2 2 1 3 1Z" fill="none" stroke="#fff" stroke-width="1.4"/></svg><span>Phone<br>555-014-2290</span></div>
  </div>
  <div class="abs vline" style="left:412px;top:60px;height:210px"></div>
  <div class="abs" style="left:481px;top:70px">
    <div class="foot-h">QUICK LINKS</div>
    <ul class="foot-links"><li>Home</li><li>Services</li><li>Research</li><li>The Institute</li><li>In the News</li></ul>
  </div>
  <div class="abs vline" style="left:677px;top:60px;height:210px"></div>
  <div class="abs brand foot-brand" style="left:745px;top:120px">
    <div class="brand-mark" style="width:72px;height:72px"></div>
    <div class="brand-name" style="font-size:34px">HOLLINBROOK<small style="font-size:15px">COUNSEL</small></div>
  </div>
  <div class="abs hr" style="top:301px"></div>
  <div class="abs copy" style="top:322px">© 2024 Hollinbrook Counsel. All Rights Reserved.</div>
</footer>

</body>
</html>
```